New Business Card for our Indoor Golf Training Facility

We are looking for designs for a new business card for our indoor golf training facility. Attached is our logo, our logo with our slogan, and here is our elevator pitch (What makes us different from the others) not sure if all the info will fit on one card, maybe you can condense the elevator pitch? here is the info

Elevator Pitch
We work with serious golfers and those that want to be serious golfers…
to make you better, faster, at all phases of the game…
We use the same state-of-the-art technology as professional golfers…
which produces data sets that shows your improvement in real time.
Our facility is available 24/7 to our members, which allows you to improve on your time.

our website: www.parkvistaswing.com

Target Market(s)

Golfers

Font styles to use
Serif
Sans Serif

Colors
ec1f27
f59195
fbd4d5
919191
d3d3d3
1b1b1b

Requirements
Must have
• our logo or our logo with the slogan, elevator pitch (can be condensed or shortened)

```html
<!DOCTYPE html>
<html lang="en">
<head>
<meta charset="utf-8">
<title>Park Vista Swing – Business Card</title>
<link href="https://fonts.googleapis.com/css2?family=Roboto:wght@400;500;700;900&display=swap" rel="stylesheet">
<style>
  :root {
    --red: #ec1f27;
    --pink: #f59195;
    --blush: #fbd4d5;
    --grey: #919191;
    --light-grey: #d3d3d3;
    --ink: #1b1b1b;
    --paper: #ffffff;
    --backdrop: #5d5e62;
  }
  * { margin: 0; padding: 0; box-sizing: border-box; }
  html, body { width: 1200px; height: 1000px; overflow: hidden; }
  body {
    background: var(--backdrop);
    font-family: "Roboto", Arial, sans-serif;
    position: relative;
  }
  .card {
    position: absolute;
    left: 250px;
    width: 700px;
    height: 400px;
    background: var(--paper);
    border-radius: 28px;
    overflow: hidden;
  }
  .card--pitch { top: 60px; }
  .card--contact { top: 540px; }

  .accent-band {
    position: absolute;
    top: 0; right: 0;
    width: 150px; height: 100%;
    background: var(--red);
  }
  .card--contact .accent-band { background: var(--blush); width: 120px; }

  .brand { position: absolute; color: var(--red); }
  .brand__name { display: block; font-weight: 900; line-height: 1; letter-spacing: 0.5px; white-space: nowrap; }
  .brand__slogan { display: block; font-weight: 400; line-height: 1.2; white-space: nowrap; }

  .card--pitch .brand { left: 40px; top: 36px; }
  .card--pitch .brand__name { font-size: 42px; }
  .card--pitch .brand__slogan { font-size: 15px; margin-top: 6px; }

  .pitch-list {
    position: absolute;
    left: 40px; top: 140px;
    width: 470px;
    list-style: none;
    color: var(--red);
    font-weight: 700;
    font-size: 16px;
    line-height: 1.2;
  }
  .pitch-list li {
    position: relative;
    padding-left: 22px;
    margin-bottom: 14px;
  }
  .pitch-list li::before {
    content: "";
    position: absolute;
    left: 0; top: 3px;
    width: 11px; height: 11px;
    border: 2px solid var(--red);
    border-radius: 50%;
  }

  .card--contact .brand { left: 40px; top: 44px; }
  .card--contact .brand__name { font-size: 58px; }
  .card--contact .brand__slogan { font-size: 21px; margin-top: 8px; }
  .rule {
    position: absolute;
    left: 40px; top: 180px;
    width: 480px; height: 2px;
    background: var(--red);
  }
  .contact-list {
    position: absolute;
    left: 40px; top: 200px;
    list-style: none;
    color: var(--ink);
    font-size: 17px;
    font-weight: 500;
  }
  .contact-list li {
    display: flex;
    align-items: center;
    gap: 10px;
    margin-bottom: 8px;
  }
  .contact-list svg { width: 16px; height: 16px; fill: var(--red); flex: none; }
  .social-handle { color: var(--red); font-weight: 700; }
</style>
</head>
<body>

  <section class="card card--pitch">
    <div class="accent-band"></div>
    <div class="brand">
      <span class="brand__name">Park Vista Swing</span>
      <span class="brand__slogan">Train Smarter. Swing Stronger. Every Day.</span>
    </div>
    <ul class="pitch-list">
      <li>We work with serious golfers and those that want to be serious golfers...</li>
      <li>We use the same state-of-the-art technology as professional golfers...</li>
      <li>Which produces data sets that shows your improvement in real time.</li>
      <li>Our facility is available 24/7 to our members, which allows you to improve on your time.</li>
    </ul>
  </section>

  <section class="card card--contact">
    <div class="accent-band"></div>
    <div class="brand">
      <span class="brand__name">Park Vista Swing</span>
      <span class="brand__slogan">Train Smarter. Swing Stronger. Every Day.</span>
    </div>
    <div class="rule"></div>
    <ul class="contact-list">
      <li>
        <svg viewBox="0 0 24 24" aria-hidden="true"><path d="M12 2a7 7 0 0 0-7 7c0 5.2 7 13 7 13s7-7.8 7-13a7 7 0 0 0-7-7zm0 9.5A2.5 2.5 0 1 1 12 6.5a2.5 2.5 0 0 1 0 5z"/></svg>
        1840 ALDER RIDGE RD. SUITE B4 MAPLEWOOD, OH 45099
      </li>
      <li>
        <svg viewBox="0 0 24 24" aria-hidden="true"><path d="M6.6 10.8a15.1 15.1 0 0 0 6.6 6.6l2.2-2.2a1 1 0 0 1 1-.25 11.4 11.4 0 0 0 3.6.57 1 1 0 0 1 1 1V20a1 1 0 0 1-1 1A17 17 0 0 1 3 4a1 1 0 0 1 1-1h3.5a1 1 0 0 1 1 1c0 1.25.2 2.45.57 3.57a1 1 0 0 1-.25 1z"/></svg>
        555-014-2290
      </li>
      <li>
        <svg viewBox="0 0 24 24" aria-hidden="true"><path d="M3 5h18a1 1 0 0 1 1 1v12a1 1 0 0 1-1 1H3a1 1 0 0 1-1-1V6a1 1 0 0 1 1-1zm9 7.2L4.2 7v1.9L12 14l7.8-5.1V7z"/></svg>
        INFO@PARKVISTASWING.COM
      </li>
      <li><span class="social-handle">@parkvistaswing</span></li>
    </ul>
  </section>

</body>
</html>
```